Casa Soleta Deli

This customer just brought a deli that is failing around me. Saw his business card and thought he needed and upgrade on them. I tasted there food and it was great! The Deli mostly sells sandwiches and hot Spanish Foods. The deli is close the beach at least 10 minutes away. So beach colors should be the theme. Please be creative

Target Market(s)

blue collar market business next to a train station

Industry/Entity Type

Food Store

Contact Information for Business Card

all the information is on the the attachment you can change the design of the card. make sure you put Hispanic foods under casa soleta deli. Be creative

Colors

Designer to choose colors to be used in the design.

Requirements
Must have
• food picture one full chicken and a Cuban-sandwich.

```html
<!DOCTYPE html>
<html lang="en">
<head>
<meta charset="utf-8">
<title>Casa Soleta Deli – Business Card</title>
<link href="https://fonts.googleapis.com/css2?family=Russo+One&family=Michroma&family=Exo+2:wght@500;600&display=swap" rel="stylesheet">
<style>
  :root {
    --stage: #232323;
    --sunset: #ee6230;
    --sun: #f9c02c;
    --ember: #e2562a;
    --ember-light: #f07a35;
    --ink: #0b0b0b;
    --amber: #f3a020;
    --footer-text: #f08a1c;
  }
  * { box-sizing: border-box; margin: 0; padding: 0; }
  html, body { width: 1189px; height: 1200px; overflow: hidden; background: var(--stage); }
  .card {
    position: absolute;
    left: 171px;
    width: 856px;
    height: 488px;
    box-shadow: 2px 2px 4px rgba(0,0,0,.5);
    overflow: hidden;
  }
  .card--front {
    top: 68px;
    background: linear-gradient(to bottom, var(--sunset) 0%, var(--sun) 52%, var(--sunset) 100%);
    text-align: center;
  }
  .front-brand { position: absolute; left: 0; right: 0; top: 180px; }
  .brand-name {
    font-family: "Russo One", sans-serif;
    color: var(--ink);
    line-height: 1;
    white-space: nowrap;
  }
  .card--front .brand-name { font-size: 64px; }
  .brand-tagline {
    font-family: "Michroma", sans-serif;
    color: var(--ink);
    text-transform: none;
    white-space: nowrap;
  }
  .card--front .brand-tagline { font-size: 26px; letter-spacing: 22px; margin-top: 10px; padding-left: 22px; }
  .front-catering {
    position: absolute; left: 0; right: 0; top: 352px;
    font-family: "Exo 2", sans-serif; font-weight: 500;
    font-size: 24px; letter-spacing: 3px; color: var(--ink);
  }

  .card--back { top: 626px; background: var(--ink); }
  .back-header {
    position: absolute; left: 0; top: 0; width: 100%; height: 182px;
    background: linear-gradient(100deg, var(--ember) 0%, var(--ember-light) 55%, var(--ember) 100%);
  }
  .back-brand { position: absolute; left: 42px; top: 52px; }
  .card--back .brand-name { font-size: 50px; }
  .card--back .brand-tagline { font-size: 21px; letter-spacing: 15px; margin-top: 6px; }
  .contact-person { position: absolute; right: 35px; top: 52px; }
  .person-name { font-family: "Russo One", sans-serif; font-size: 40px; color: var(--ink); line-height: 1; }
  .person-phone {
    display: flex; align-items: center; gap: 8px; margin-top: 10px;
    font-family: "Russo One", sans-serif; font-size: 26px; color: var(--ink);
  }
  .stripe { position: absolute; left: 0; width: 100%; }
  .stripe--top { top: 190px; height: 5px; background: var(--amber); }
  .stripe--bottom { top: 412px; height: 8px; background: var(--amber); }
  .photo-row {
    position: absolute; top: 203px; left: 0; width: 100%; height: 204px;
    display: grid; grid-template-columns: repeat(4, 1fr); gap: 5px;
  }
  .photo { height: 100%; }
  .photo--chicken { background: linear-gradient(160deg, #6b4a20, #b0702a 60%, #3a2210); }
  .photo--wings { background: linear-gradient(160deg, #7a3c1a, #a45a2a 50%, #c9b9c0); }
  .photo--platter { background: linear-gradient(160deg, #c9902f, #e6c36a 50%, #5a7a2a); }
  .photo--sandwich { background: linear-gradient(160deg, #d9a060, #b86060 50%, #e8d6a0); }
  .back-footer {
    position: absolute; left: 0; bottom: 0; width: 100%; height: 68px;
    display: flex; align-items: center; justify-content: center; gap: 14px;
    font-family: "Exo 2", sans-serif; font-weight: 500; font-size: 24px;
    color: var(--footer-text);
  }
  .back-footer b { font-weight: 600; }
</style>
</head>
<body>
  <section class="card card--front">
    <div class="front-brand">
      <div class="brand-name">Casa Soleta Deli</div>
      <div class="brand-tagline">Hispanic foods</div>
    </div>
    <p class="front-catering">we offer catering for</p>
  </section>

  <section class="card card--back">
    <header class="back-header">
      <div class="back-brand">
        <div class="brand-name">Casa Soleta Deli</div>
        <div class="brand-tagline">Hispanic foods</div>
      </div>
      <div class="contact-person">
        <div class="person-name">Marco Reyes</div>
        <div class="person-phone">
          <svg width="26" height="26" viewBox="0 0 26 26" aria-hidden="true">
            <rect width="26" height="26" fill="#0b0b0b"/>
            <path d="M9 6c1 0 2 2 2.5 3.5.3.8-1 1.5-1 2.2.5 1.6 1.6 3 3 3.6.6 0 1.3-1.2 2-1 1.5.5 3.5 1.5 3.5 2.5 0 1.2-1.6 2.7-3 2.7C10.5 19.5 6.5 15 6.5 9 6.5 7.5 7.8 6 9 6z" fill="#f07a35"/>
          </svg>
          <span>0198 765 432</span>
        </div>
      </div>
    </header>
    <div class="stripe stripe--top"></div>
    <div class="photo-row">
      <div class="photo photo--chicken" role="img" aria-label="Photo of a whole roasted chicken on a wooden board"></div>
      <div class="photo photo--wings" role="img" aria-label="Photo of fried chicken with coleslaw"></div>
      <div class="photo photo--platter" role="img" aria-label="Photo of a platter with tacos, fried yuca and empanadas"></div>
      <div class="photo photo--sandwich" role="img" aria-label="Photo of a pressed Cuban sandwich"></div>
    </div>
    <div class="stripe stripe--bottom"></div>
    <footer class="back-footer">
      <span><b>E:</b> hello@casasoleta.com</span>
      <span>|</span>
      <span><b>W:</b> www.casasoletadeli.com</span>
    </footer>
  </section>
</body>
</html>
```